5 Banner für die Startseite der Hompage
Zielgruppe
Wir sind eine 'kreative' kleine Truppe, die mit neuen Ideen versuchen wollen, auch mal andere Wege in den Projekten zu gehen.
unsere neue Webseite lautet
Aufgabenstellung
Auf meiner Webseite www.kavelorn.de habe ich bereits einen ersten Vorschlag eingefügt.
Es geht um die 5 Banner auf der Startseite; diese sollen sowohl Designtechnisch als auch optisch sehr ansprechend wirken, um das Interesse potentieller Kunden zu wecken.
Meine Farben habe ich mit angehängt.
Der Text könnte sich noch anpassen, muss aber mit in den Banner aufgenommen werden.
Breite sollte 1200Pixel; Höhe 600Pixel

```html
<!DOCTYPE html>
<html lang="de">
<head>
<meta charset="utf-8">
<title>Kavelorn – Startseite</title>
<link rel="stylesheet" href="https://fonts.googleapis.com/css2?family=Carlito:ital,wght@0,400;0,700;1,400&family=Lato:wght@400;900&display=swap">
<style>
  :root {
    --pink: #ee4a8e;
    --pink-soft: #f78cb8;
    --pink-dark: #a9235a;
    --ink: #3a464c;
    --white: #ffffff;
    --section-bg: #f7f8f8;
    --hero-top: #8a5e5c;
    --hero-mid: #6b5558;
    --hero-bottom: #5e6274;
    --gold-light: #d9c08a;
    --gold: #a98a4e;
    --gold-dark: #4d3f27;
  }
  * { margin: 0; padding: 0; box-sizing: border-box; }
  html, body { width: 1200px; height: 606px; overflow: hidden; background: var(--section-bg); }
  .page { position: relative; width: 1200px; height: 606px; overflow: hidden; }

  .hero {
    position: absolute; left: 0; top: 0; width: 1200px; height: 481px;
    background: linear-gradient(180deg, var(--hero-top) 0%, var(--hero-mid) 45%, var(--hero-bottom) 100%);
  }

  .brand {
    position: absolute; left: 190px; top: 11px;
    font-family: "Carlito", sans-serif; font-weight: 700; font-size: 20px;
    color: var(--white); letter-spacing: 0.2px;
  }
  .main-nav {
    position: absolute; top: 17px; left: 678px;
    display: flex; gap: 14px;
    font-family: "Lato", sans-serif; font-size: 9px; color: var(--white);
  }

  .slide {
    position: absolute; left: 184px; top: 80px; width: 788px; height: 361px;
    background: var(--white); overflow: hidden;
    box-shadow: 0 8px 16px rgba(0,0,0,0.45);
  }
  .slide-rings { position: absolute; left: 0; top: 0; }
  .slide-visual {
    position: absolute; right: 0; top: 0; width: 132px; height: 361px;
    background: linear-gradient(160deg, var(--gold-light) 0%, var(--gold) 45%, var(--gold-dark) 100%);
    clip-path: polygon(22% 0, 100% 0, 100% 100%, 0 100%, 10% 60%, 4% 40%);
  }
  .quote-mark {
    position: absolute; font-family: "Carlito", sans-serif; font-style: italic; font-weight: 700;
    color: var(--pink); line-height: 1;
  }
  .quote-mark.open { left: 25px; top: 84px; font-size: 100px; }
  .quote-mark.close { left: 306px; top: 136px; font-size: 76px; }
  .quote {
    position: absolute; left: 76px; top: 68px;
    font-family: "Carlito", sans-serif; font-size: 31px; line-height: 38.5px; color: var(--ink);
  }
  .quote-author {
    position: absolute; left: 349px; top: 162px;
    font-family: "Carlito", sans-serif; font-style: italic; font-size: 16px; color: var(--ink);
  }
  .slide-text {
    position: absolute; left: 71px; top: 266px;
    font-family: "Carlito", sans-serif; font-size: 13px; line-height: 16.5px; color: var(--ink);
  }
  .read-more {
    position: absolute; left: 69px; top: 320px;
    font-family: "Carlito", sans-serif; font-weight: 700; font-size: 19px;
    color: var(--pink); text-decoration: none;
  }

  .slide-arrow {
    position: absolute; top: 236px; width: 34px; height: 49px;
    background: var(--pink); color: var(--white);
    font-family: "Lato", sans-serif; font-weight: 900; font-size: 28px;
    display: flex; align-items: center; justify-content: center;
  }
  .slide-arrow.prev { left: 174px; }
  .slide-arrow.next { left: 949px; }
  .arrow-fold { position: absolute; top: 224px; width: 10px; height: 12px; }
  .arrow-fold.prev { left: 174px; background: var(--pink-dark); clip-path: polygon(100% 0, 100% 100%, 0 100%); }
  .arrow-fold.next { left: 973px; background: var(--pink-dark); clip-path: polygon(0 0, 100% 100%, 0 100%); }

  .section-title {
    position: absolute; left: 0; width: 1156px; top: 538px; text-align: center;
    font-family: "Lato", sans-serif; font-weight: 900; font-size: 31px; color: var(--ink);
    letter-spacing: 0.3px;
  }
  .divider { position: absolute; left: 549px; top: 589px; }
</style>
</head>
<body>
<div class="page">
  <header class="hero" role="img" aria-label="Hintergrundbild: technische Zeichnung mit Rasterlinien in rotbraunen und blaugrauen Tönen"></header>

  <div class="brand">Kavelorn</div>
  <nav class="main-nav">
    <span>Home</span><span>Unser Ansatz</span><span>Produkte</span><span>Dienstleistungen</span><span>Schulungen</span>
  </nav>

  <section class="slide">
    <svg class="slide-rings" width="788" height="361" viewBox="0 0 788 361">
      <path fill="var(--pink-soft)" fill-rule="evenodd"
        d="M404,-36 a119,119 0 1,0 238,0 a119,119 0 1,0 -238,0 Z M440,-36 a83,83 0 1,0 166,0 a83,83 0 1,0 -166,0 Z"/>
      <path fill="var(--pink-soft)" fill-rule="evenodd"
        d="M-243,325 a146,146 0 1,0 292,0 a146,146 0 1,0 -292,0 Z M-205,325 a108,108 0 1,0 216,0 a108,108 0 1,0 -216,0 Z"/>
    </svg>
    <div class="slide-visual" role="img" aria-label="Foto: goldene Zahnräder eines Uhrwerks"></div>

    <span class="quote-mark open">”</span>
    <p class="quote">Was man lernen muss,<br>um es zu tun, das lernt man,<br>indem man es tut.</p>
    <span class="quote-mark close">”</span>
    <span class="quote-author">Aristoteles</span>

    <p class="slide-text">Unserer Schulung sind an Ihren Themen und Anwendungen ausgerichtet.<br>Besonders liegen uns Konzepte am Herzen, die Sie in Ihrer Arbeit begleiten.</p>
    <a class="read-more" href="#">&gt;&gt; Lesen Sie mehr</a>
  </section>

  <span class="arrow-fold prev"></span>
  <span class="slide-arrow prev">&lt;</span>
  <span class="arrow-fold next"></span>
  <span class="slide-arrow next">&gt;</span>

  <h2 class="section-title">UNSER ANSATZ</h2>
  <svg class="divider" width="58" height="12" viewBox="0 0 58 12" stroke="var(--ink)" stroke-width="3" stroke-linecap="round">
    <path d="M3,2 L11,10 M11,2 L3,10"/>
    <path d="M21,2 L29,10 M29,2 L21,10"/>
    <path d="M39,2 L47,10 M47,2 L39,10"/>
  </svg>
</div>
</body>
</html>
```